KVO-Business Card Design

I need a modern, professional business card design that includes my logo as the main feature, maybe the entire background with the contact info overlaying or even contact info on the back and the logo full frontal

Neat and organized placement of contact information

Would like to see options in black and white

Target Market(s)

real estate Developers, Construction managers, business and home owners

Industry/Entity Type

Construction

Contact Information for Business Card

KVO Construction
Danny Ferrante
General Contractor

Office: 1-888-902-7315 Ext #1
Cell: 215-730-4162
Fax: 1-888-902-7315

Font styles to use
Serif

Requirements
Must have
• title
• office #
• cell #
• Email
• website
Nice to have
• fax

```html
<!DOCTYPE html>
<html lang="en">
<head>
<meta charset="utf-8">
<title>KVO-Business Card Design</title>
<link href="https://fonts.googleapis.com/css2?family=PT+Serif:wght@400;700&display=swap" rel="stylesheet">
<style>
  :root {
    --backdrop: #e9e6e2;
    --card: #2b2b2b;
    --green: #2f9a45;
    --green-light: #5cc24a;
    --ink: #f2f2f2;
  }
  * { margin: 0; padding: 0; box-sizing: border-box; }
  html, body {
    width: 1200px; height: 1000px; overflow: hidden;
    background: var(--backdrop);
    font-family: "PT Serif", Georgia, serif;
  }
  .card {
    position: absolute; left: 265px; width: 667px; height: 398px;
    background: var(--card);
    box-shadow: 0 4px 14px rgba(0,0,0,.25);
  }
  .card--front { top: 73px; }
  .card--back { top: 532px; }

  .holder { position: absolute; top: 140px; left: 0; right: 0; text-align: center; }
  .holder__name {
    color: var(--green); font-weight: 700; font-size: 22px;
    letter-spacing: .4px; line-height: 1.2; text-transform: uppercase;
  }
  .holder__title { color: var(--ink); font-size: 15px; margin-top: 2px; }

  .contacts {
    position: absolute; left: 0; right: 0;
    display: flex; justify-content: center; gap: 22px;
    color: var(--ink); font-size: 15px; line-height: 20px;
  }
  .contacts--phones { top: 214px; }
  .contacts--online { top: 242px; }
  .contacts__item { display: flex; align-items: center; gap: 6px; white-space: nowrap; }
  .contacts__item svg { width: 14px; height: 14px; fill: var(--green); flex: none; }

  .front-mark {
    position: absolute; bottom: 28px; left: 0; right: 0;
    text-align: center; color: var(--green);
    font-weight: 700; font-size: 30px; letter-spacing: 1px;
  }

  .brand {
    position: absolute; inset: 0;
    display: flex; align-items: center; justify-content: center; gap: 16px;
  }
  .brand__square { width: 34px; height: 34px; background: var(--green-light); }
  .brand__name {
    color: var(--green-light); font-weight: 700; font-size: 46px; letter-spacing: 1px;
  }
</style>
</head>
<body>
  <section class="card card--front">
    <div class="holder">
      <p class="holder__name">Danny Ferrante</p>
      <p class="holder__title">General Contractor</p>
    </div>
    <div class="contacts contacts--phones">
      <span class="contacts__item">
        <svg viewBox="0 0 12 14" aria-hidden="true" style="width:12px"><path d="M3 0h2v3h4a1 1 0 0 1 1 1v9a1 1 0 0 1-1 1H3a1 1 0 0 1-1-1V4a1 1 0 0 1 1-1zM4 5v3h4V5z"/></svg>
        215-730-4162
      </span>
      <span class="contacts__item">
        <svg viewBox="0 0 14 14" aria-hidden="true"><path d="M1 4q6-4 12 0v2h-3V4.5H4V6H1zM3 7h8l2 5H1z"/></svg>
        1-888-902-7315 Ext #1
      </span>
      <span class="contacts__item">
        <svg viewBox="0 0 14 14" aria-hidden="true"><path d="M4 1h6v4H4zM1 6h12v5h-2V9H3v2H1zM4 10h6v3H4z"/></svg>
        1-888-902-7315
      </span>
    </div>
    <div class="contacts contacts--online">
      <span class="contacts__item">
        <svg viewBox="0 0 14 14" aria-hidden="true"><path d="M1 3h12v8H1zM2 4v.5l5 3.5 5-3.5V4L7 7.2z"/></svg>
        danny@kvoconstruction.com
      </span>
      <span class="contacts__item">
        <svg viewBox="0 0 14 14" aria-hidden="true"><path d="M7 1a6 6 0 1 0 0 12A6 6 0 0 0 7 1zm0 1.3c.8.9 1.3 2.4 1.4 4H5.6C5.7 4.7 6.2 3.2 7 2.3zM2.4 7.7h2c.1 1.4.5 2.7 1.1 3.6a4.7 4.7 0 0 1-3.1-3.6zm0-1.4a4.7 4.7 0 0 1 3.1-3.6c-.6.9-1 2.2-1.1 3.6zm3.2 1.4h2.8c-.1 1.6-.6 3.1-1.4 4-.8-.9-1.3-2.4-1.4-4zm3.9 3.6c.6-.9 1-2.2 1.1-3.6h2a4.7 4.7 0 0 1-3.1 3.6zm1.1-5c-.1-1.4-.5-2.7-1.1-3.6a4.7 4.7 0 0 1 3.1 3.6z"/></svg>
        www.kvoconstruction.com
      </span>
    </div>
    <p class="front-mark">KVO Construction</p>
  </section>

  <section class="card card--back">
    <div class="brand">
      <span class="brand__square"></span>
      <span class="brand__name">KVO Construction</span>
    </div>
  </section>
</body>
</html>
```